New management consulting website

I need a 4-5 page website that I can manage in WordPress on Hostlane.example for a new management consulting company. The website is www.torvik-example.com and the company name is Torvik Group LLC. The attached spec has an example of a draft site, layout and actual copy and includes company and contact information. I have more high-res images I can send.

Must include instruction/assistance loading the site to my WordPress dashboard.

Target Market(s)

Any business, especially SAAS

Industry/Entity Type

Consultant

Coding

Coded - Design and coding required

Number of Pages Required

4 page

Font styles to use
Sans Serif

Colors
0456a4

Requirements
Must have
• Modern and stylish

```html
<!DOCTYPE html>
<html lang="en">
<head>
<meta charset="utf-8">
<title>Torvik Consulting — Above and Beyond</title>
<link rel="stylesheet" href="https://fonts.googleapis.com/css2?family=Montserrat:wght@400;500;600;700&family=Syncopate:wght@700&display=swap">
<style>
  :root {
    --navy: #1e3f6a;
    --navy-text: #1f3d66;
    --accent-bar: #2a5d8f;
    --ink: #111111;
    --white: #ffffff;
  }
  * { margin: 0; padding: 0; box-sizing: border-box; }
  html, body { width: 1200px; height: 578px; overflow: hidden; }
  body {
    position: relative;
    font-family: "Montserrat", Arial, sans-serif;
    color: var(--ink);
    background: #f7f3ee;
  }
  .hero-backdrop {
    position: absolute; inset: 0 0 43px 0;
    background: linear-gradient(100deg, #fbf9f5 0%, #f6f1ea 50%, #e9e6e2 64%, #8e8f92 72%, #1b1b1b 80%, #000 100%);
  }
  .site-header { position: absolute; left: 161px; top: 15px; width: 878px; height: 70px; }
  .brand-name {
    position: absolute; left: 0; top: 22px;
    font-family: "Montserrat", Arial, sans-serif;
    font-weight: 600; font-size: 26px; line-height: 30px;
    letter-spacing: 2px; color: var(--navy-text); text-transform: uppercase;
  }
  .menu-toggle {
    position: absolute; right: 0; top: 17px; width: 34px; height: 34px;
    background: var(--navy); border: 0; border-radius: 3px;
    display: flex; flex-direction: column; justify-content: center; align-items: center; gap: 5px;
  }
  .menu-toggle span { display: block; width: 18px; height: 2px; background: var(--white); }
  .intro {
    position: absolute; left: 161px; top: 232px; width: 520px;
    border-left: 2px solid var(--accent-bar); padding-left: 20px;
  }
  .intro-title {
    font-family: "Syncopate", "Arial Black", sans-serif;
    font-weight: 700; font-size: 31px; line-height: 34px; letter-spacing: 0;
    color: var(--ink); margin-bottom: 20px; white-space: nowrap;
  }
  .intro-lead { font-size: 15.5px; line-height: 24px; letter-spacing: 0.4px; margin-bottom: 8px; white-space: nowrap; }
  .intro-lead strong { font-weight: 700; }
  .intro-body { width: 465px; font-size: 15.5px; line-height: 26.5px; letter-spacing: 0.6px; }
  .site-footer {
    position: absolute; left: 0; bottom: 0; width: 1200px; height: 43px;
    background: var(--navy); color: var(--white);
    display: flex; align-items: center; justify-content: space-between;
    padding: 0 161px;
  }
  .copyright { font-size: 13px; letter-spacing: 0.2px; }
  .social-links { display: flex; gap: 14px; }
  .social-links span {
    display: block; width: 12px; height: 12px; border-radius: 50%; background: var(--white);
  }
</style>
</head>
<body>
  <div class="hero-backdrop" role="img" aria-label="Photo of two climbers helping each other up a dark rocky peak against a hazy misty mountain sky"></div>

  <header class="site-header">
    <div class="brand-name">Torvik Consulting</div>
    <button class="menu-toggle" aria-label="Open menu"><span></span><span></span><span></span></button>
  </header>

  <section class="intro">
    <h1 class="intro-title">ABOVE AND BEYOND</h1>
    <p class="intro-lead">The word <strong>‘Torvik’</strong> originates It means <strong>‘above. beyond’.</strong></p>
    <p class="intro-body">At Torvik Consulting our approach is to you rise above day-to-day business challenges. and build unique. innovative solutions to move beyond them.</p>
  </section>

  <footer class="site-footer">
    <p class="copyright">Copyright 2021 Torvik Consulting. All Rights Reserved.</p>
    <nav class="social-links" aria-label="Social links">
      <span aria-label="Social profile one"></span>
      <span aria-label="Social profile two"></span>
      <span aria-label="Social profile three"></span>
    </nav>
  </footer>
</body>
</html>
```